marketing flier needed - ONE SIDED

We are presently in the process of creating a marketing campaign, in which we will be distributing swag packs to our branches across the United States. These packs will include a range of items such as hats, shirts, beef jerky, peanuts, cups, and more. We require a marketing flier for internal use to inform our branch managers about this program. Our intention is to announce this program at the annual meeting. I kindly request the flier to be provided in digital format by January 21st, so that we can produce copies and send them out.

I will provide a mock-up of the flier that the CEO has prepared. As we are in the initial stages, we currently do not possess any images of the items. Additionally, I will also include the existing fliers that are currently being used.

Target Market(s)

roofers /construction workers

Industry/Entity Type

roofing materials construction

Font styles to use
Other font styles liked:
• does not matter - most of the customer are men so nothing girly

Colors
0054AA
0677BA
7BADD7
CADEEF
E8F1F8

Requirements
Must have
• a variety of marketing items with our logo

```html
<!DOCTYPE html>
<html lang="en">
<head>
<meta charset="utf-8">
<title>Get The Swag! 2024 Flier</title>
<link href="https://fonts.googleapis.com/css2?family=Poppins:wght@400;500;600;700;800&display=swap" rel="stylesheet">
<style>
  :root {
    --navy: #2b3990;
    --navy-deep: #232f7e;
    --royal: #3548a8;
    --silver-light: #f4f4f6;
    --silver-mid: #c9cbd1;
    --silver-dark: #9a9ca3;
    --paper: #ffffff;
    --stage: #efefef;
    --gold: #d9a42b;
    --ink: #2b3990;
  }
  * { margin: 0; padding: 0; box-sizing: border-box; }
  html, body { width: 1200px; height: 3308px; overflow: hidden; background: var(--stage); }
  body { position: relative; font-family: "Poppins", sans-serif; color: var(--ink); }

  .flier {
    position: absolute; left: 90px; top: 992px;
    width: 1021px; height: 1324px;
    background: var(--paper); overflow: hidden;
    box-shadow: 0 6px 24px rgba(0,0,0,0.12);
  }
  .header-shape { position: absolute; left: 0; top: 0; width: 1021px; height: 414px; }

  .eagle-photo {
    position: absolute; left: 151px; top: 12px; width: 180px; height: 150px;
    border-radius: 40% 60% 50% 50%;
    background: radial-gradient(ellipse at 60% 55%, #6b5640 0%, #4a3b2c 45%, rgba(43,57,144,0) 75%);
  }
  .headline-year {
    position: absolute; left: 360px; top: 62px;
    font-weight: 800; font-size: 104px; line-height: 1; color: #fff; letter-spacing: -1px;
  }
  .headline-lead {
    position: absolute; left: 160px; top: 196px;
    font-weight: 800; font-size: 56px; line-height: 50px; color: #fff;
    background: linear-gradient(180deg, #ffffff 0%, var(--silver-mid) 100%);
    -webkit-background-clip: text; background-clip: text; -webkit-text-fill-color: transparent;
  }
  .headline-main {
    position: absolute; left: 300px; top: 160px;
    font-weight: 800; font-size: 172px; line-height: 1; letter-spacing: -2px;
    background: linear-gradient(180deg, #ffffff 0%, #e3e4e8 45%, var(--silver-dark) 100%);
    -webkit-background-clip: text; background-clip: text; -webkit-text-fill-color: transparent;
  }

  .products-photo {
    position: absolute; left: 85px; top: 480px; width: 640px; height: 550px;
    border-radius: 12px;
    background: linear-gradient(160deg, #3548a8 0%, #2b3990 35%, #d9dbe2 60%, #c7ab8f 80%, #f1f1f3 100%);
    opacity: 0.9;
  }
  .box-lettering {
    position: absolute; left: 425px; top: 430px; width: 200px; height: 100px;
    background: rgba(43,57,144,0.12); border-radius: 10px; z-index: 2;
  }
  .pointer-arrow { position: absolute; left: 560px; top: 540px; width: 70px; height: 110px; z-index: 2; }

  .packs-title {
    position: absolute; left: 709px; top: 478px; width: 240px; height: 40px;
    background: var(--navy); color: #fff; border-radius: 9px;
    font-weight: 700; font-size: 21px; line-height: 40px; text-align: center; letter-spacing: 0.3px;
  }
  .packs-list { position: absolute; left: 718px; top: 550px; list-style: none; }
  .packs-list li {
    display: flex; align-items: center; gap: 14px;
    font-size: 34px; font-weight: 400; color: var(--navy); height: 63px;
  }
  .packs-list li:nth-child(n+4) { padding-left: 6px; }
  .packs-list svg { width: 30px; height: 30px; flex: none; }

  .announcement {
    position: absolute; left: 0; top: 1060px; width: 1021px; height: 126px;
    background: var(--navy); color: #fff;
    display: flex; align-items: center; justify-content: center; text-align: center;
    font-size: 27px; line-height: 34px; font-weight: 400; padding: 0 40px;
  }

  .brand-name {
    position: absolute; left: 48px; top: 1212px; width: 260px; height: 92px;
    display: flex; align-items: center; justify-content: center; gap: 12px;
    font-weight: 700; font-size: 22px; color: var(--navy);
  }
  .brand-name .brand-dot { width: 16px; height: 16px; border-radius: 50%; background: var(--navy); flex: none; }

  .contact-pill {
    position: absolute; left: 355px; width: 372px; height: 40px;
    border: 1.5px solid var(--silver-mid); border-radius: 20px;
    display: flex; align-items: center; gap: 12px;
    font-size: 19px; color: var(--navy); font-weight: 500;
  }
  .contact-pill .contact-icon {
    width: 40px; height: 40px; border-radius: 50%; background: var(--navy);
    display: flex; align-items: center; justify-content: center; margin-left: -1.5px; flex: none;
  }
  .contact-pill svg { width: 22px; height: 22px; }
  .contact-web { top: 1210px; }
  .contact-mail { top: 1268px; }

  .social-label {
    position: absolute; left: 795px; top: 1216px; width: 168px; height: 24px;
    background: var(--navy); color: #fff; border-radius: 6px;
    font-size: 12px; font-weight: 700; text-align: center; line-height: 24px;
  }
  .social-handle {
    position: absolute; left: 760px; top: 1246px; width: 240px; text-align: center;
    font-size: 19px; color: var(--navy);
  }
  .social-marks {
    position: absolute; left: 828px; top: 1284px; display: flex; gap: 14px;
  }
  .social-marks span { width: 22px; height: 22px; border-radius: 50%; background: var(--royal); display: block; }
</style>
</head>
<body>
  <main class="flier">
    <svg class="header-shape" viewBox="0 0 1021 414" preserveAspectRatio="none" aria-hidden="true">
      <defs>
        <linearGradient id="silverBand" x1="0" x2="1" y1="0" y2="0">
          <stop offset="0" stop-color="#b9bbc2"/>
          <stop offset="0.5" stop-color="#eeeef1"/>
          <stop offset="1" stop-color="#a6a8af"/>
        </linearGradient>
        <linearGradient id="headerBlue" x1="0" x2="0" y1="0" y2="1">
          <stop offset="0" stop-color="#2e3d96"/>
          <stop offset="1" stop-color="#26348a"/>
        </linearGradient>
      </defs>
      <path d="M0 0 H1021 V350 C760 330 420 350 0 382 Z" fill="url(#silverBand)"/>
      <path d="M0 0 H1021 V340 C760 320 420 335 0 370 Z" fill="#ffffff"/>
      <path d="M0 0 H1021 V334 C760 312 420 325 0 360 Z" fill="url(#headerBlue)"/>
      <path d="M0 396 C420 352 760 338 1021 358 V370 C760 350 420 366 0 414 Z" fill="url(#silverBand)"/>
    </svg>

    <div class="eagle-photo" role="img" aria-label="Photo of a bald eagle in flight"></div>
    <div class="headline-year">2024</div>
    <div class="headline-lead">GET<br>THE</div>
    <div class="headline-main">SWAG!</div>

    <div class="products-photo" role="img" aria-label="Product photo: branded blue t-shirt, open shipping box, beef jerky pouch, nut assortment, beanie, cowboy hat and mugs"></div>
    <div class="box-lettering" role="img" aria-label="Handwritten note: Boxes To Put Swag In!"></div>
    <svg class="pointer-arrow" viewBox="0 0 70 110" aria-hidden="true">
      <path d="M20 6 C60 20 62 70 30 96" fill="none" stroke="#8c8e95" stroke-width="2.5" stroke-linecap="round"/>
      <path d="M28 80 L30 97 L46 92" fill="none" stroke="#8c8e95" stroke-width="2.5" stroke-linecap="round" stroke-linejoin="round"/>
    </svg>

    <div class="packs-title">PACKS INCLUDE</div>
    <ul class="packs-list">
      <li><svg viewBox="0 0 30 30" aria-hidden="true"><circle cx="13" cy="16" r="11" fill="none" stroke="var(--gold)" stroke-width="2.5"/><path d="M7 16 L12 21 L27 6" fill="none" stroke="var(--navy)" stroke-width="3" stroke-linecap="round" stroke-linejoin="round"/></svg>Hats</li>
      <li><svg viewBox="0 0 30 30" aria-hidden="true"><circle cx="13" cy="16" r="11" fill="none" stroke="var(--gold)" stroke-width="2.5"/><path d="M7 16 L12 21 L27 6" fill="none" stroke="var(--navy)" stroke-width="3" stroke-linecap="round" stroke-linejoin="round"/></svg>Shirts</li>
      <li><svg viewBox="0 0 30 30" aria-hidden="true"><circle cx="13" cy="16" r="11" fill="none" stroke="var(--gold)" stroke-width="2.5"/><path d="M7 16 L12 21 L27 6" fill="none" stroke="var(--navy)" stroke-width="3" stroke-linecap="round" stroke-linejoin="round"/></svg>Cups</li>
      <li><svg viewBox="0 0 30 30" aria-hidden="true"><circle cx="13" cy="16" r="11" fill="none" stroke="var(--gold)" stroke-width="2.5"/><path d="M7 16 L12 21 L27 6" fill="none" stroke="var(--navy)" stroke-width="3" stroke-linecap="round" stroke-linejoin="round"/></svg>Beef Jerky</li>
      <li><svg viewBox="0 0 30 30" aria-hidden="true"><circle cx="13" cy="16" r="11" fill="none" stroke="var(--gold)" stroke-width="2.5"/><path d="M7 16 L12 21 L27 6" fill="none" stroke="var(--navy)" stroke-width="3" stroke-linecap="round" stroke-linejoin="round"/></svg>Peanuts</li>
      <li><svg viewBox="0 0 30 30" aria-hidden="true"><circle cx="13" cy="16" r="11" fill="none" stroke="var(--gold)" stroke-width="2.5"/><path d="M7 16 L12 21 L27 6" fill="none" stroke="var(--navy)" stroke-width="3" stroke-linecap="round" stroke-linejoin="round"/></svg>And More</li>
    </ul>

    <p class="announcement">each banch will get a qustesly shipent of sag/logoes itrms long<br>with presentstons swag boes to give out to customers</p>

    <div class="brand-name"><span class="brand-dot"></span>Harborline Supply</div>

    <div class="contact-pill contact-web">
      <span class="contact-icon"><svg viewBox="0 0 24 24" aria-hidden="true"><circle cx="12" cy="12" r="9" fill="none" stroke="#fff" stroke-width="1.6"/><ellipse cx="12" cy="12" rx="4" ry="9" fill="none" stroke="#fff" stroke-width="1.6"/><path d="M3 12 H21 M5 7 H19 M5 17 H19" stroke="#fff" stroke-width="1.4"/></svg></span>
      www.harborlinesupply.com
    </div>
    <div class="contact-pill contact-mail">
      <span class="contact-icon"><svg viewBox="0 0 24 24" aria-hidden="true"><rect x="3" y="6" width="18" height="12" rx="1.5" fill="none" stroke="#fff" stroke-width="1.6"/><path d="M3 7 L12 14 L21 7" fill="none" stroke="#fff" stroke-width="1.6"/></svg></span>
      info@harborlinesupply.com
    </div>

    <div class="social-label">CONNECT WITH US</div>
    <div class="social-handle">@HarborlineSupply</div>
    <div class="social-marks" aria-label="Social media profiles"><span></span><span></span><span></span></div>
  </main>
</body>
</html>
```